Project Sign for Construction Company

Site contractor needs a 4'x8' sign to place on construction sites for advertising. Our company builds the infrastructure for new housing developments. These sign will be posted on the road side to be viewed by passing cars. I want a clean and bold look and feel that resembles my company logo.

Font styles to use
Other font styles liked:
• Hypatia Sans Pro

Colors

Designer to choose colors to be used in the design.

Requirements
Must have
• 555-382-9146 | Info@MarlowPaving.example
• CUC 8047319
• www.MarlowPaving.example
• Services
• Road Construction
• Site Preparation & Excavation
• Underground Utilities
• Shoreline Restoration
Nice to have
• Now Hiring
• Pipe Layers
• Foremen
• Equipment Operators
Should not have
• Should not have stock picture images used in the design, focus on logo and geometric shapes

```html
<!DOCTYPE html>
<html lang="en">
<head>
<meta charset="utf-8">
<title>Marlow Paving – Site Sign</title>
<link rel="stylesheet" href="https://fonts.googleapis.com/css2?family=Alegreya+Sans:wght@400;500;700;800&display=swap">
<style>
  :root {
    --sign-bg: #f0f0f2;
    --brand-blue: #0054a0;
    --panel-gray: #59595b;
    --text-gray: #58585a;
    --ink: #231f20;
    --white: #ffffff;
    --facet-light: #d6d6d9;
    --facet-dark: #88898d;
  }
  * { box-sizing: border-box; margin: 0; padding: 0; }
  html, body { width: 1200px; height: 695px; overflow: hidden; }
  body {
    background: var(--sign-bg);
    font-family: "Alegreya Sans", "Trebuchet MS", sans-serif;
    position: relative;
  }
  .sign { position: absolute; inset: 0; background: var(--sign-bg); overflow: hidden; }

  .facets {
    position: absolute;
    background: linear-gradient(135deg, var(--facet-light) 0%, var(--facet-dark) 100%);
  }
  .facets--top {
    right: 0; top: 0; width: 112px; height: 94px;
    clip-path: polygon(40% 0, 100% 0, 100% 100%, 0 50%);
    opacity: .85;
  }
  .facets--bottom {
    right: 0; bottom: 0; width: 215px; height: 250px;
    clip-path: polygon(100% 0, 100% 100%, 0 100%, 0 70%, 40% 25%);
  }

  .brand {
    position: absolute; left: 52px; top: 250px; width: 360px;
    display: flex; flex-direction: column; align-items: center; gap: 18px;
  }
  .brand__square { width: 64px; height: 64px; background: var(--brand-blue); }
  .brand__name {
    color: var(--brand-blue); font-weight: 800; font-size: 60px;
    line-height: .95; text-align: center; letter-spacing: 2px; text-transform: uppercase;
  }

  .license {
    position: absolute; right: 42px; top: 128px;
    font-size: 27px; font-weight: 500; color: var(--ink); letter-spacing: .5px;
  }

  .services-tab {
    position: absolute; left: 473px; top: 165px; width: 210px; height: 45px;
    background: var(--brand-blue);
    clip-path: polygon(0 0, 92% 0, 100% 100%, 0 100%);
    color: var(--white); font-weight: 700; font-size: 36px; line-height: 47px;
    padding-left: 14px; letter-spacing: .5px;
  }
  .services {
    position: absolute; left: 475px; top: 222px; width: 424px; height: 293px;
    background: var(--brand-blue); padding: 22px 0 0 42px;
    list-style: none; color: var(--white);
  }
  .services__item {
    position: relative; font-weight: 500; font-size: 28px; line-height: 1.28;
    letter-spacing: .6px; text-transform: uppercase; margin-bottom: 12px;
  }
  .services__item::before {
    content: ""; position: absolute; left: -24px; top: 10px;
    width: 7px; height: 7px; border-radius: 50%; background: var(--white);
  }

  .hiring {
    position: absolute; left: 909px; top: 222px; width: 268px; height: 293px;
    background: var(--panel-gray); color: var(--white); padding: 80px 0 0 25px;
  }
  .hiring__badge {
    display: inline-block; border: 1.5px solid var(--white);
    font-weight: 800; font-size: 22px; letter-spacing: .5px;
    padding: 3px 10px 0 8px; line-height: 31px; margin-bottom: 14px;
  }
  .hiring__roles { list-style: none; }
  .hiring__role {
    font-size: 23px; font-weight: 400; line-height: 1.2; padding-bottom: 5px;
    margin-bottom: 10px; width: 150px; white-space: nowrap;
  }
  .hiring__role--ruled { border-bottom: 1px solid var(--white); }

  .contact {
    position: absolute; left: 49px; top: 604px;
    font-size: 31px; font-weight: 700; color: var(--text-gray); letter-spacing: .3px;
    white-space: nowrap;
  }
  .contact__divider { color: var(--brand-blue); margin: 0 10px; }
</style>
</head>
<body>
  <main class="sign">
    <div class="facets facets--top" role="img" aria-label="Faceted grey geometric shapes"></div>
    <div class="facets facets--bottom" role="img" aria-label="Faceted grey geometric shapes"></div>

    <div class="brand">
      <span class="brand__square"></span>
      <span class="brand__name">Marlow<br>Paving</span>
    </div>

    <p class="license">CUC 8047319</p>

    <h2 class="services-tab">SERVICES</h2>
    <ul class="services">
      <li class="services__item">Road Construction</li>
      <li class="services__item">Site Preparation &amp;<br>Excavation</li>
      <li class="services__item">Underground Utilities</li>
      <li class="services__item">Shoreline Restoration</li>
    </ul>

    <section class="hiring">
      <h3 class="hiring__badge">NOW HIRING</h3>
      <ul class="hiring__roles">
        <li class="hiring__role hiring__role--ruled">Pipe Layers</li>
        <li class="hiring__role hiring__role--ruled">Foremen</li>
        <li class="hiring__role">Equipment Operators</li>
      </ul>
    </section>

    <p class="contact">555-382-9146<span class="contact__divider">|</span>Info@MarlowPaving.example<span class="contact__divider">|</span>www.MarlowPaving.example</p>
  </main>
</body>
</html>
```